International Travel & Visas Firm needs a Schengen Visa eBook Cover Design

We need an ebook cover design for an online based travel, immigration, visas & nationality law firm called 'OrV' (ordinance and relocation). We are all about helping people overcome the obstacles to travel and ensuring that people achieve their dreams and ambitions through travel to various destinations and bettering their lives.This initial ebook cover is for our downloaded pdf ebook all about Schengen visas and travelling to any of the 26 European countries that form the Schengen Zone.We want people to be excited about buying this book even before receiving it.We would like to see amazing designs that also speak to our logo and new branding.Check out https://ordinanceandrelocation.example/schengen-visas/ and http://ordinanceandrelocation.pages.funnelkit.example/start-your-schengen-visa-application

Target Market(s)

Travellers that want to get a visa to travel around Europe

Industry/Entity Type

Travel Industry

Colors
fbee3d
faa54b

Requirements
Must have
• - Title:
• Schengen Visa Guide
Nice to have
• - tagline:
• Liberate yourself and travel to 26 European Countries
• - OrV Logo
• - Reference to it being an insider's guide to Schengen Visas
• - a play on the word OrV (I am)

```html
<!DOCTYPE html>
<html lang="en">
<head>
<meta charset="utf-8">
<title>Schengen Visa Guide – eBook Cover</title>
<link rel="stylesheet" href="https://fonts.googleapis.com/css2?family=Oswald:wght@500;600&family=Roboto+Condensed:wght@500&display=swap">
<style>
  :root {
    --page: #ffffff;
    --cover-dark: #0d100c;
    --cover-mid: #1f2a1c;
    --passport: #c9b4a2;
    --passport-deep: #8c7566;
    --title-yellow: #f5ea3c;
    --title-orange: #f8a54c;
    --tagline: #ffffff;
    --badge-bg: #ffffff;
    --badge-ink: #4a4a4a;
  }
  html, body {
    margin: 0;
    padding: 0;
    width: 1200px;
    height: 1200px;
    overflow: hidden;
    background: var(--page);
  }
  .canvas {
    position: relative;
    width: 1200px;
    height: 1200px;
  }
  .cover {
    position: absolute;
    left: 305px;
    top: 152px;
    width: 610px;
    height: 914px;
    overflow: hidden;
    background: var(--cover-dark);
  }
  .cover-photo {
    position: absolute;
    inset: 0;
    background:
      radial-gradient(ellipse 260px 360px at 150px 640px, var(--passport) 0%, var(--passport-deep) 55%, rgba(0,0,0,0) 100%),
      radial-gradient(ellipse 420px 300px at 380px 320px, var(--cover-mid) 0%, var(--cover-dark) 100%);
  }
  .cover-title {
    position: absolute;
    inset: 0;
    width: 610px;
    height: 914px;
  }
  .cover-title text {
    font-family: "Oswald", "Arial Narrow", sans-serif;
    font-weight: 500;
  }
  .title-schengen { fill: var(--title-yellow); font-size: 72px; }
  .title-visa { fill: var(--title-orange); font-size: 308px; }
  .title-guide { fill: var(--title-yellow); font-size: 134px; }
  .tagline {
    position: absolute;
    left: 363px;
    top: 512px;
    margin: 0;
    width: 190px;
    color: var(--tagline);
    font-family: "Roboto Condensed", "Arial Narrow", sans-serif;
    font-weight: 500;
    font-size: 29px;
    line-height: 38px;
  }
  .brand-badge {
    position: absolute;
    left: 418px;
    top: 772px;
    width: 192px;
    height: 103px;
    background: var(--badge-bg);
    border-radius: 52px 0 0 52px;
    display: flex;
    flex-direction: column;
    align-items: center;
    justify-content: center;
    color: var(--badge-ink);
    font-family: "Oswald", "Arial Narrow", sans-serif;
    font-weight: 500;
  }
  .brand-name {
    display: flex;
    align-items: center;
    gap: 8px;
    font-size: 44px;
    line-height: 1;
  }
  .brand-mark {
    width: 12px;
    height: 12px;
    border-radius: 50%;
    background: var(--badge-ink);
  }
  .brand-descriptor {
    margin-top: 6px;
    font-size: 12px;
    line-height: 1;
  }
</style>
</head>
<body>
<div class="canvas">
  <section class="cover">
    <div class="cover-photo" role="img" aria-label="Photograph of a hand holding an open passport with travel stamps against a dark blurred background"></div>

    <svg class="cover-title" viewBox="0 0 610 914" aria-label="Schengen Visa Guide">
      <text class="title-schengen" x="48" y="88" textLength="268" lengthAdjust="spacingAndGlyphs">SCHENGEN</text>
      <text class="title-visa" x="51" y="342" textLength="508" lengthAdjust="spacingAndGlyphs">VISA</text>
      <text class="title-guide" x="282" y="469" textLength="280" lengthAdjust="spacingAndGlyphs">GUIDE</text>
    </svg>

    <p class="tagline">Liberate yourself and travel to 26 European Countries</p>

    <div class="brand-badge">
      <div class="brand-name"><span class="brand-mark"></span>OrV</div>
      <div class="brand-descriptor">ordinance and relocation</div>
    </div>
  </section>
</div>
</body>
</html>
```